" Consultório de pediatria geral onde 3 médicos atendem. Eu, meu irmão e meu pai. Atendemos de recém-nascidos até adolescentes. Também faço atendimento na sala de parto e vacinas. "

```html
<!DOCTYPE html>
<html lang="pt-BR">
<head>
<meta charset="UTF-8">
<title>Moreti Pediatria – Pasta</title>
<link rel="stylesheet" href="https://fonts.googleapis.com/css2?family=Cinzel:wght@400;500&family=Open+Sans:wght@400;600&display=swap">
<style>
  :root {
    --bg: #e4e4e4;
    --paper: #ffffff;
    --blue: #3560c8;
    --blue-dark: #2a4fb3;
    --blue-light: #4070d6;
    --teal: #1fb3a6;
    --ink-blue: #2d55bd;
    --white: #ffffff;
  }
  * { margin: 0; padding: 0; box-sizing: border-box; }
  html, body { width: 1200px; height: 1200px; overflow: hidden; background: var(--bg); }
  .folder { position: absolute; left: 130px; top: 170px; width: 940px; height: 860px; display: flex; }
  .panel { position: relative; width: 470px; height: 860px; }
  .panel-inside { background: var(--paper); }
  .panel-cover {
    background: linear-gradient(160deg, var(--blue-light) 0%, var(--blue) 45%, var(--blue-dark) 100%);
    display: flex; flex-direction: column; align-items: center;
  }
  .glue-flap { position: absolute; left: -70px; top: 0; width: 70px; height: 860px; }
  .pocket { position: absolute; left: 0; bottom: 0; width: 470px; height: 200px; }
  .brand { display: flex; flex-direction: column; align-items: center; font-family: "Cinzel", serif; }
  .brand-mark { border-radius: 50%; background: var(--teal); }
  .brand-name { font-weight: 500; letter-spacing: 0.04em; line-height: 1; }
  .brand-sub { font-weight: 500; letter-spacing: 0.32em; line-height: 1; }
  .inside-brand { position: absolute; left: 0; right: 0; top: 560px; color: var(--ink-blue); }
  .inside-brand .brand-mark { width: 48px; height: 48px; margin-bottom: 10px; }
  .inside-brand .brand-name { font-size: 34px; }
  .inside-brand .brand-sub { font-size: 11px; margin-top: 5px; }
  .contact-band {
    position: absolute; left: 0; top: 648px; width: 470px; height: 30px;
    background: var(--teal); color: var(--white);
    font-family: "Open Sans", sans-serif; font-size: 9px;
    display: flex; align-items: center; justify-content: space-between; padding: 0 14px;
  }
  .contact-item { display: flex; align-items: center; gap: 6px; line-height: 1.15; }
  .contact-item svg { width: 11px; height: 11px; fill: var(--white); flex: none; }
  .cover-brand { margin-top: 300px; color: var(--white); }
  .cover-brand .brand-mark { width: 96px; height: 96px; margin-bottom: 14px; }
  .cover-brand .brand-name { font-size: 62px; }
  .cover-brand .brand-sub { font-size: 20px; margin-top: 6px; }
  .cover-accent {
    position: absolute; left: 300px; top: 560px; width: 180px; height: 180px;
    border-radius: 50%; background: rgba(255,255,255,0.06);
  }
</style>
</head>
<body>
  <div class="folder">
    <section class="panel panel-inside">
      <svg class="glue-flap" viewBox="0 0 70 860" aria-hidden="true">
        <path d="M70 480 L30 500 L30 560 L8 575 L8 640 L30 655 L30 860 L70 860 Z" fill="#2f59c2"/>
      </svg>
      <div class="brand inside-brand">
        <div class="brand-mark"></div>
        <div class="brand-name">MORETI</div>
        <div class="brand-sub">PEDIATRIA</div>
      </div>
      <div class="contact-band">
        <div class="contact-item">
          <svg viewBox="0 0 24 24"><path d="M6.6 10.8a15.1 15.1 0 0 0 6.6 6.6l2.2-2.2a1 1 0 0 1 1-.25 11.4 11.4 0 0 0 3.6.57 1 1 0 0 1 1 1V20a1 1 0 0 1-1 1A17 17 0 0 1 3 4a1 1 0 0 1 1-1h3.5a1 1 0 0 1 1 1c0 1.25.2 2.45.57 3.57a1 1 0 0 1-.25 1Z"/></svg>
          <span>(11) 4520-3187</span>
        </div>
        <div class="contact-item">
          <svg viewBox="0 0 24 24"><path d="M2 5h20v14H2Zm2 2v.5l8 5 8-5V7Z"/></svg>
          <span>contato@moreti.com.br</span>
        </div>
        <div class="contact-item">
          <svg viewBox="0 0 24 24"><path d="M12 3 2 12h3v8h5v-5h4v5h5v-8h3Z"/></svg>
          <span>Rua das Acácias, 210<br>São Paulo - SP - 01234-000</span>
        </div>
      </div>
      <svg class="pocket" viewBox="0 0 470 200" aria-hidden="true">
        <defs>
          <linearGradient id="pocketFill" x1="0" y1="0" x2="0" y2="1">
            <stop offset="0" stop-color="#3a66cf"/>
            <stop offset="1" stop-color="#2b50b5"/>
          </linearGradient>
        </defs>
        <path d="M0 20 L470 20 L470 200 L0 200 Z" fill="url(#pocketFill)"/>
        <path d="M0 20 L470 20 L470 40 C360 40 300 60 250 110 C215 145 200 175 195 200 L0 200 Z" fill="#ffffff" opacity="0.08"/>
      </svg>
    </section>
    <section class="panel panel-cover">
      <div class="cover-accent"></div>
      <div class="brand cover-brand">
        <div class="brand-mark"></div>
        <div class="brand-name">MORETI</div>
        <div class="brand-sub">PEDIATRIA</div>
      </div>
    </section>
  </div>
</body>
</html>
```